DOUBLE SIDED BROCHURE NEEDED TO PROMOTE DOCTOR

I need a double sided DL size (99mm x 210mm) brochure, promoting a doctor seeing patients in a new area.

I want something professional. I have included the relevant information. I would also like the Dr's picture somwhere in the brochure, with a professional background. I wish to print these tomorrow, so i will pick a winner within 14 hours of posting this ad.

I have included an example of a brochures design that I recently saw, and its definietly a good starting point.

Medical

```html
<!DOCTYPE html>
<html lang="en">
<head>
<meta charset="utf-8">
<title>Dr. Samir Haddad – Bayview Surgical Consulting</title>
<link rel="stylesheet" href="https://fonts.googleapis.com/css2?family=Handlee&family=Mulish:ital,wght@0,300;0,400;0,700;0,800;1,800&display=swap">
<style>
  :root {
    --charcoal: #4a4a4a;
    --slate: #6e6e6e;
    --amber: #f4b23c;
    --ochre: #dc9230;
    --ink: #1e1e1e;
    --white: #ffffff;
    --mist-top: #e6e6e6;
    --mist-bottom: #ffffff;
  }
  * { margin: 0; padding: 0; box-sizing: border-box; }
  html, body {
    width: 1200px;
    height: 1200px;
    overflow: hidden;
    background: var(--white);
  }
  .brochure {
    position: relative;
    width: 1200px;
    height: 1200px;
    overflow: hidden;
  }
  .shapes, .portrait-area {
    position: absolute;
    left: 0;
    top: 0;
    width: 1200px;
    height: 1200px;
  }
  .announcement {
    position: absolute;
    left: 36px;
    top: 142px;
    width: 420px;
    font-family: "Handlee", cursive;
    font-size: 25px;
    line-height: 31.5px;
    color: var(--white);
    white-space: nowrap;
  }
  .announcement .salutation { color: var(--amber); margin-bottom: 4px; }
  .announcement p + p { margin-top: 17px; }
  .announcement .salutation + p { margin-top: 4px; }

  .clinic-details {
    position: absolute;
    left: 36px;
    top: 758px;
    width: 360px;
    font-family: "Mulish", sans-serif;
    font-weight: 700;
    color: var(--ink);
    font-size: 28.5px;
    line-height: 35px;
  }
  .clinic-details .phone-label { margin-top: 22px; }
  .clinic-details .phone-number {
    font-size: 40px;
    font-weight: 800;
    line-height: 48px;
    margin-top: 6px;
  }
  .clinic-details .divider {
    width: 326px;
    border-top: 2px dotted var(--white);
    margin: 16px 0 20px;
  }
  .clinic-details .fax-number {
    font-size: 39px;
    font-weight: 800;
    line-height: 50px;
    margin-top: 8px;
  }

  .services {
    position: absolute;
    left: 550px;
    top: 724px;
    width: 640px;
    font-family: "Mulish", sans-serif;
    color: var(--white);
  }
  .services .lead, .services .sublead {
    font-style: italic;
    font-weight: 800;
    color: var(--ink);
    font-size: 22px;
    line-height: 30px;
    white-space: nowrap;
  }
  .services ul {
    list-style: none;
    font-weight: 300;
    font-size: 23px;
    line-height: 26.6px;
    white-space: nowrap;
  }
  .services li { position: relative; padding-left: 18px; }
  .services li::before {
    content: "•";
    position: absolute;
    left: 0;
  }
  .services li.continued::before { content: ""; }
  .specialties { margin: 12px 0 0 108px; }
  .sublead { margin: 30px 0 0 206px; }
  .general { margin: 24px 0 0 269px; }
</style>
</head>
<body>
<main class="brochure">
  <svg class="shapes" viewBox="0 0 1200 1200" aria-hidden="true">
    <defs>
      <linearGradient id="mist" x1="0" y1="0" x2="0" y2="1">
        <stop offset="0" stop-color="var(--mist-top)"/>
        <stop offset="1" stop-color="var(--mist-bottom)"/>
      </linearGradient>
    </defs>

    <rect class="front-header" x="0" y="0" width="1200" height="100" fill="url(#mist)"/>
    <polygon class="front-text-panel" points="5,100 302,100 577,540 5,540" fill="var(--charcoal)"/>
    <polygon class="front-accent-triangle" points="184,100 246,0 302,100" fill="var(--ochre)"/>
    <polygon class="front-diagonal-band" points="246,0 367,0 690,540 570,540" fill="var(--amber)"/>
    <polygon class="front-corner-sliver" points="1083,0 1103,0 1163,100 1146,100" fill="var(--charcoal)"/>
    <polygon class="front-corner-accent" points="1103,0 1200,0 1200,100 1163,100" fill="var(--amber)"/>
    <polygon class="front-footer-strip" points="5,540 347,540 332,564 5,564" fill="var(--amber)"/>

    <rect class="back-header" x="0" y="588" width="1200" height="104" fill="url(#mist)"/>
    <polygon class="back-contact-panel" points="5,692 325,692 621,1172 5,1172" fill="var(--amber)"/>
    <polygon class="back-accent-triangle" points="194,692 262,588 325,692" fill="var(--charcoal)"/>
    <polygon class="back-diagonal-band" points="262,588 387,588 742,1172 621,1172" fill="var(--slate)"/>
    <polygon class="back-services-panel" points="463,690 1200,690 1200,1172 756,1172" fill="var(--ochre)"/>
    <polygon class="back-corner-accent" points="1182,588 1200,588 1200,618" fill="var(--charcoal)"/>
    <polygon class="back-footer-strip" points="5,1172 371,1172 355,1200 5,1200" fill="var(--charcoal)"/>
  </svg>

  <svg class="portrait-area" viewBox="0 0 1200 1200" role="img"
       aria-label="Photo of Dr. Samir Haddad smiling in glasses and a dark jacket, in front of a modern hospital building under a blue sky">
    <defs>
      <linearGradient id="portrait-tones" x1="0" y1="0" x2="1" y2="1">
        <stop offset="0" stop-color="#b9cbe0"/>
        <stop offset="0.45" stop-color="#6f7780"/>
        <stop offset="1" stop-color="#2d2f38"/>
      </linearGradient>
    </defs>
    <polygon points="440,100 1200,100 1200,540 703,540" fill="url(#portrait-tones)"/>
  </svg>

  <section class="announcement">
    <p class="salutation">Dear Doctors,</p>
    <p>We are pleased to announce<br>that Dr.Samir Haddad is now<br>consulting in Bayview,<br>seeing public and private<br>patients.</p>
    <p>Guaranteed appointment within two<br>weeks, with patients having the option<br>of surgery at Coastal Health Campus,<br>Southgate Hospital or<br>St.Clement Westfield.</p>
  </section>

  <section class="clinic-details">
    <p>Bayview Clinic:<br>42 Harbourline Road<br>Bayview WA 6299.</p>
    <p class="phone-label">Phone:</p>
    <p class="phone-number">1300 000 482</p>
    <div class="divider"></div>
    <p>Please send all referrals<br>by fax to</p>
    <p class="fax-number">(08) 5550 2714`</p>
  </section>

  <section class="services">
    <p class="lead">Dr.Haddad is a highly trained specialised surgeon, in all<br>areas of Endocrine, Breast and General Surgery. Including;</p>
    <ul class="specialties">
      <li>Thyroid Surgery</li>
      <li>Parathyroid surgery (including minimally invasive<br>parathyroidectomy)</li>
      <li>Breast Cancer</li>
      <li class="continued">Benign breast lesions</li>
    </ul>
    <p class="sublead">All areas of general surgery, such as;</p>
    <ul class="general">
      <li>Gallbladder surgery</li>
      <li>Hernia surgery</li>
      <li>Haemorrhoids</li>
      <li>Carpal Tunnel</li>
      <li>Vasectomy etc etc…</li>
    </ul>
  </section>
</main>
</body>
</html>
```